Brindlewood Institute Course Brochure

Brindlewood Institute is a private institution providing different courses for students internationally.
We need a series of brochures for 5 new courses individually.(5 pieces in total)
We have opened 5 courses
1. Higher Diploma in Construction & Civil engineering
2.Higher Diploma in Quantity Surveying
3.Higher Diploma in Mechanical Engineering
4.Higher Diploma in Electrical & Electronic Engineering
5.Higher Diploma in Facilities Management

Please give out the design sample using one of the course, then drag and adjust accordingly for other courses

Requirement
*Vibrant and energetic looking
*Size A5 double sided/A4 size double fold
*Please include the given company logo and Learnsafe image
*Refer to "Higher Diploma synopsis" file for course description
*information must be clear to see
*Entry requirements modules and other course details must be included in
*Redesign according to the attached files
* a PSD file is attached for reference and obtain information
Updates

Target Market(s)

International students above 21 years old

Industry/Entity Type

Education

Font styles to use
Sans Serif

Requirements
Must have
• *Please include the given company logo and Learnsafe image
• *Summarise the descriptions, do not be wordy.
• *information must be clear to see
• *Entry requirements modules and other course details must be included in
• *attached file for reference
Nice to have
• More catchy images and designs
• Keep it simple
• It is on designer's choice of color, does not have to use only company colours.

```html
<!DOCTYPE html>
<html lang="en">
<head>
<meta charset="utf-8">
<title>Brindlewood Institute – Higher Diploma in Mechanical Engineering</title>
<link rel="stylesheet" href="https://fonts.googleapis.com/css2?family=Open+Sans:wght@400;600;700&family=PT+Serif:wght@400;700&display=swap">
<style>
:root{
  --bg:#e4e2e3;
  --paper:#ffffff;
  --blue:#1f6fb8;
  --blue-dark:#1b4f8a;
  --navy:#23285e;
  --yellow:#f7b21b;
  --grey-text:#5e5e66;
  --dark-text:#2a2a33;
  --red:#e2332a;
  --rule:#c9ccd6;
  --tint:#eef0f6;
}
*{box-sizing:border-box;margin:0;padding:0}
html,body{width:1200px;height:799px;overflow:hidden;background:var(--bg)}
body{position:relative;font-family:"Open Sans",Arial,sans-serif;color:var(--dark-text)}
.page{position:absolute;top:78px;width:450px;height:648px;background:var(--paper);overflow:hidden}
.page--front{left:132px}
.page--back{left:654px;width:438px;background:linear-gradient(180deg,#fff 0,#fff 15%,var(--tint) 100%)}
.brand{position:absolute;display:flex;align-items:center;gap:6px}
.brand__dot{width:30px;height:30px;border-radius:50%;background:var(--navy)}
.brand__name{font-weight:700;font-size:10px;color:var(--navy);width:70px;line-height:1.15}
.badge{position:absolute;right:30px;top:24px;display:flex;align-items:center;gap:6px}
.badge__mark{width:30px;height:30px;border-radius:50%;background:var(--red)}
.badge__name{font-weight:700;font-size:14px;color:var(--dark-text)}
.badge__meta{position:absolute;right:30px;top:60px;font-size:5px;color:var(--grey-text);width:90px;line-height:1.3}
.stripe{position:absolute;left:0;width:100%;height:10px}
.hero{position:absolute;left:0;top:112px;width:100%;height:240px;background:linear-gradient(135deg,#f3f4f7 0%,#c8ccd4 45%,#7d838e 75%,#e6e8ec 100%)}
.title-band{position:absolute;left:0;top:366px;width:100%;height:30px;background:var(--blue);color:#fff;font-family:"PT Serif",Georgia,serif;font-weight:700;font-size:16px;text-align:center;line-height:30px}
.front-copy{position:absolute;left:0;top:404px;width:100%;height:196px;padding:8px 28px;background:linear-gradient(180deg,#fff,#e9ebf1);font-family:"PT Serif",Georgia,serif;color:var(--grey-text)}
.front-copy p{font-size:7.2px;line-height:1.45;margin-bottom:9px}
.front-copy .lead{font-size:10.2px;line-height:1.4;color:#3a3d48;margin-top:6px}
.front-footer{position:absolute;left:0;bottom:0;width:100%;height:46px;display:flex}
.front-footer__web{flex:0 0 58%;background:var(--yellow);color:#fff;font-weight:600;font-size:9px;letter-spacing:2px;display:flex;align-items:center;padding-left:18px}
.front-footer__call{flex:1;background:var(--blue);color:#fff;display:flex;align-items:center;gap:10px;padding-left:12px}
.front-footer__call strong{font-weight:400;font-size:12.5px}
.front-footer__call span{font-size:8.5px;line-height:1.35}
.section-head{position:absolute;display:flex;align-items:center;gap:5px;font-weight:700;color:var(--navy)}
.section-head svg{flex:none}
.modules{position:absolute;left:18px;top:112px;width:402px;border-collapse:collapse;font-size:5.8px}
.modules th{color:#fff;font-weight:700;height:12px;font-size:6.6px}
.modules th.y{background:var(--yellow)}
.modules th.b{background:var(--blue)}
.modules td{border:0.6px solid var(--rule);height:12.2px;padding:0 4px;background:#fff}
.modules td.c{text-align:center}
.modules .hl{color:var(--red)}
.facts{position:absolute;left:16px;top:294px;width:410px;display:flex;gap:6px}
.fact{width:25%}
.fact h3{display:flex;align-items:center;gap:4px;font-size:8.6px;color:var(--navy);font-weight:700}
.fact p{font-size:5.8px;line-height:1.45;padding-left:12px;color:var(--grey-text)}
.entry{position:absolute;left:16px;top:366px;width:406px;height:168px;background:#fff;border:0.6px solid var(--rule);padding:8px 10px;font-size:5.8px;color:var(--grey-text)}
.entry li{list-style:none;position:relative;padding-left:10px;line-height:1.45;margin-bottom:7px}
.entry li::before{content:"";position:absolute;left:0;top:2.5px;border-left:4px solid var(--navy);border-top:2.5px solid transparent;border-bottom:2.5px solid transparent}
.entry__note{position:absolute;right:8px;bottom:5px;font-style:italic;font-size:4.8px}
.back-footer{position:absolute;left:0;bottom:0;width:100%;height:44px;background:var(--blue);color:#fff;font-size:5.8px}
.back-footer__yellow{position:absolute;right:0;top:0;width:45%;height:100%;background:var(--yellow);clip-path:polygon(8% 0,100% 0,100% 100%,0 100%)}
.back-footer__contacts{position:absolute;left:14px;top:6px;line-height:1.55}
.back-footer__addr{position:absolute;left:250px;top:6px;line-height:1.4;color:var(--navy);font-weight:600;display:flex;gap:4px}
.back-footer__social{position:absolute;right:12px;bottom:8px;display:flex;align-items:center;gap:3px;color:var(--navy);font-weight:600}
.back-footer__social i{width:6px;height:6px;background:var(--navy)}
</style>
</head>
<body>

<section class="page page--front">
  <div class="brand" style="left:30px;top:26px">
    <span class="brand__dot"></span><span class="brand__name">Brindlewood Institute</span>
  </div>
  <div class="badge"><span class="badge__mark"></span><span class="badge__name">Learnsafe</span></div>
  <div class="badge__meta">Cert No: LS-0000<br>Valid: 2016 - 2019</div>
  <svg class="stripe" style="top:92px" viewBox="0 0 450 10" preserveAspectRatio="none" aria-hidden="true">
    <rect width="450" height="10" fill="var(--yellow)"/>
    <polygon points="230,0 450,0 450,10 220,10" fill="var(--blue)"/>
  </svg>
  <div class="hero" role="img" aria-label="Close-up of metal gears and bearings resting on engineering blueprints"></div>
  <svg class="stripe" style="top:352px;height:14px" viewBox="0 0 450 14" preserveAspectRatio="none" aria-hidden="true">
    <polygon points="300,14 320,0 450,0 450,14" fill="var(--yellow)"/>
    <polygon points="0,8 290,8 284,14 0,14" fill="var(--blue-dark)"/>
  </svg>
  <h1 class="title-band">Higher Diploma in Mechanical Engineering</h1>
  <div class="front-copy">
    <p>Mechanical Engineering is needed in a wide area of application in the engineering industry. It is applicable in automotive, energy sectors to construction and biomedical industries. Modern day mechanical engineering uses innovative design and technologies to develop cutting-edge products and systems.</p>
    <p>The course emphasise design, analysis, and manufacturing new products and technologies. It addresses the society's needs by combining mechanical engineering fundamentals with innovative ideas. We structure our curriculum by emphasizing engineering theory and technical skills. Our students learn how to analyze solve practical problem.</p>
    <p class="lead">Graduates from this course can look forward to a career in Construction industry – designs and builds infrastructure, buildings and buildings services, Rail industry – design, construct, manage and maintain rail system components from trains and tracks to electrical power systems and train control systems.</p>
  </div>
  <footer class="front-footer">
    <div class="front-footer__web">www.brindlewood.edu.example</div>
    <div class="front-footer__call"><strong>CALL NOW</strong><span>+65 6100 2040<br>+65 9100 3050</span></div>
  </footer>
</section>

<section class="page page--back">
  <div class="brand" style="left:36px;top:20px">
    <span class="brand__dot"></span><span class="brand__name">Brindlewood Institute</span>
  </div>
  <svg class="stripe" style="top:74px" viewBox="0 0 438 10" preserveAspectRatio="none" aria-hidden="true">
    <rect width="438" height="10" fill="var(--yellow)"/>
    <polygon points="250,0 438,0 438,10 240,10" fill="var(--blue)"/>
  </svg>
  <div class="section-head" style="left:20px;top:92px;font-size:10px">
    <svg width="10" height="10" viewBox="0 0 10 10" aria-hidden="true"><polygon points="0,0 10,5 0,10" fill="var(--blue)"/></svg>Module Assessment
  </div>
  <table class="modules">
    <tr><th class="y" style="width:17%">HDME</th><th class="b">Modules</th><th class="y" style="width:11%">Credits</th><th class="b" style="width:28%">Distribution</th></tr>
    <tr><td>IEP201</td><td>Introduction to Electrical Principles</td><td class="c">20</td><td class="hl">30% exam 70% Coursework</td></tr>
    <tr><td>IMP202</td><td>Introduction to Mechanical Principles</td><td class="c">20</td><td>100% coursework</td></tr>
    <tr><td>FD203</td><td>Fluid Dynamics</td><td class="c">20</td><td>100% coursework</td></tr>
    <tr><td>WSH204</td><td>Workplace Safety and Health Practice</td><td class="c">20</td><td>100% coursework</td></tr>
    <tr><td>GEDA205</td><td>Green Engineering Design and Application</td><td class="c">20</td><td>100% coursework</td></tr>
    <tr><td>PC206</td><td>Professions in Context</td><td class="c">20</td><td>100% coursework</td></tr>
    <tr><td>HTC301</td><td>Heat Transfer and Combustion</td><td class="c">20</td><td>100% coursework</td></tr>
    <tr><td>AM302</td><td>Applied Mechanics</td><td class="c">20</td><td class="hl">100% Examination</td></tr>
    <tr><td>RT303</td><td>Robotics Technology</td><td class="c">20</td><td>100% coursework</td></tr>
    <tr><td>CADA304</td><td>Computer Aided Design and Analysis</td><td class="c">20</td><td>100% coursework</td></tr>
    <tr><td>MEM305</td><td>Material and Energy Management</td><td class="c">20</td><td>100% coursework</td></tr>
    <tr><td>PPP306</td><td>Professional Practice Project</td><td class="c">20</td><td>100% coursework</td></tr>
  </table>
  <div class="facts">
    <div class="fact"><h3><svg width="8" height="8" viewBox="0 0 10 10" aria-hidden="true"><polygon points="0,0 10,5 0,10" fill="var(--blue)"/></svg>Duration &amp; Time</h3>
      <p>Full Time: 20 Months<br>Part Time: 24 Months<br>Sunday:9AM-5PM<br>Weekdays: 7PM-10PM<br>&nbsp;&nbsp;&nbsp;&nbsp;&nbsp;&nbsp;&nbsp;*twice a week</p></div>
    <div class="fact"><h3><svg width="8" height="8" viewBox="0 0 10 10" aria-hidden="true"><polygon points="0,0 10,5 0,10" fill="var(--blue)"/></svg>Course Fee</h3>
      <p>Part Time<br>Full Payment: S$9,900<br>Registration: S$100<br>Instalment: 2,12,24 months plan</p></div>
    <div class="fact"><h3><svg width="8" height="8" viewBox="0 0 10 10" aria-hidden="true"><polygon points="0,0 10,5 0,10" fill="var(--blue)"/></svg>Awarded by</h3>
      <p>Higher Diploma in Mechanical Engineering By Brindlewood Institute</p></div>
    <div class="fact"><h3><svg width="8" height="8" viewBox="0 0 10 10" aria-hidden="true"><polygon points="0,0 10,5 0,10" fill="var(--blue)"/></svg>Intake</h3>
      <p>Every 2 Months</p></div>
  </div>
  <div class="section-head" style="left:30px;top:352px;font-size:9px">Entry Requirement</div>
  <ul class="entry">
    <li>Minimum 21 years and above.</li>
    <li>'A' Level 3 subjects passes, English plus any other subjects or; a related Diploma from local Polytechnic or; other CPE registered PEI or equivalent (Diplomas from other countries)</li>
    <li>IELTS 5.5 or equivalent</li>
    <li>Student with other diploma qualifications with minimum age of 23 years with at least 3 years working experience in relevant field. Recognition of Prior Learning (RPL) will be done to analysis whether student has met the required skills to be admitted onto our Higher Diplomas.</li>
    <li>Matured students, of 30 years old with at least 8 years of working experience will be considered on an individual basis</li>
    <span class="entry__note">*All fees excluding GST</span>
  </ul>
  <footer class="back-footer">
    <div class="back-footer__yellow"></div>
    <div class="back-footer__contacts">☏ +65 6100 2041<br>☎ +65 6100 2040 / +65 9100 3050<br>info@brindlewood.edu.example / admissions@brindlewood.edu.example</div>
    <div class="back-footer__addr">
      <svg width="7" height="9" viewBox="0 0 10 13" aria-hidden="true"><path d="M5 0a5 5 0 0 1 5 5c0 3.5-5 8-5 8S0 8.5 0 5a5 5 0 0 1 5-5z" fill="var(--navy)"/><circle cx="5" cy="5" r="2" fill="var(--yellow)"/></svg>
      <span>48, Harbourline Road<br>Tower 2, Meridian Park,<br>Singapore 100482</span>
    </div>
    <div class="back-footer__social"><i></i>Follow Us On</div>
  </footer>
</section>

</body>
</html>
```